BRIM Outreach Partners Business Card Rebrand

Hello Designers! We are looking for help designing our new business card to go in conjunction with our company rebrand. Unfortunately, we have an event mid June that requires we get these printed ASAP (before our new website is launched.) We have a mostly complete Brand Book which I have uploaded to this request for your reference to company information, style, fonts. I've also enclosed our logo file in .eps & .jpg. Attached is a sample business card my boss liked but said was "too simple." I made it in Canva and do not profess to be a designer. NOT FOR DESIGN REFERENCE, ONLY FOR CONTEXT Here is what our old website looks like: https://brimoutreachpartners.com/.

```html
<!DOCTYPE html>
<html lang="en">
<head>
<meta charset="utf-8">
<title>BRIM Outreach Partners – Business Card</title>
<link rel="stylesheet" href="https://fonts.googleapis.com/css2?family=Montserrat:wght@400;500;700;800&family=Roboto+Condensed:wght@400;500&display=swap">
<style>
  :root {
    --bg: #7f97b8;
    --sky: #6bbbe8;
    --sky-light: #84c9ef;
    --ink: #161616;
    --paper: #ffffff;
    --muted: #3a3a3a;
  }
  * { margin: 0; padding: 0; box-sizing: border-box; }
  html, body { width: 1200px; height: 876px; overflow: hidden; }
  body {
    background: var(--bg);
    font-family: "Montserrat", Arial, sans-serif;
    position: relative;
  }
  .card {
    position: absolute;
    top: 288px;
    width: 525px;
    height: 300px;
    overflow: hidden;
    box-shadow: 0 6px 18px rgba(30, 45, 80, 0.35);
  }
  .card--front { left: 50px; background: var(--paper); }
  .card--back {
    left: 625px;
    background: linear-gradient(135deg, var(--sky-light), var(--sky));
    display: flex;
    align-items: center;
    justify-content: center;
  }
  .card__shapes { position: absolute; inset: 0; }

  .holder {
    position: absolute;
    right: 40px;
    top: 40px;
    text-align: right;
    color: var(--ink);
  }
  .holder__name {
    font-size: 17px;
    font-weight: 700;
    letter-spacing: 0.5px;
    text-transform: uppercase;
  }
  .holder__name span { font-weight: 400; }
  .holder__role {
    font-size: 9px;
    font-weight: 500;
    letter-spacing: 1.2px;
    text-transform: uppercase;
    color: var(--muted);
    margin-top: 2px;
  }

  .brand {
    display: flex;
    align-items: center;
    gap: 10px;
  }
  .brand__dot {
    flex: none;
    border-radius: 50%;
    background: var(--sky);
  }
  .brand__name {
    font-weight: 800;
    color: var(--ink);
    text-transform: uppercase;
    line-height: 1.05;
  }
  .card--front .brand { position: absolute; left: 150px; top: 112px; }
  .card--front .brand__dot { width: 30px; height: 30px; }
  .card--front .brand__name { font-size: 20px; letter-spacing: 0.5px; }
  .card--back .brand__dot { width: 58px; height: 58px; background: var(--paper); }
  .card--back .brand__name { font-size: 34px; letter-spacing: 0.5px; }

  .contacts {
    position: absolute;
    left: 0;
    right: 0;
    bottom: 22px;
    display: flex;
    font-family: "Roboto Condensed", Arial Narrow, sans-serif;
    color: var(--paper);
    font-size: 12px;
  }
  .contact {
    display: flex;
    flex-direction: column;
    align-items: center;
    gap: 8px;
    padding: 0 10px;
  }
  .contact + .contact { border-left: 1px solid rgba(255, 255, 255, 0.8); }
  .contact--email { width: 195px; }
  .contact--phone { width: 120px; }
  .contact--place { width: 210px; }
  .contact__icon { width: 16px; height: 16px; }
</style>
</head>
<body>

<section class="card card--front" aria-label="Business card front">
  <svg class="card__shapes" viewBox="0 0 525 300" aria-hidden="true">
    <defs>
      <linearGradient id="band" x1="0" y1="0" x2="1" y2="1">
        <stop offset="0" stop-color="#84c9ef"/>
        <stop offset="1" stop-color="#62b5e5"/>
      </linearGradient>
      <linearGradient id="edge" x1="0" y1="0" x2="1" y2="1">
        <stop offset="0" stop-color="#111"/>
        <stop offset="0.45" stop-color="#d6d6d6"/>
        <stop offset="0.7" stop-color="#555"/>
        <stop offset="1" stop-color="#111"/>
      </linearGradient>
    </defs>
    <path d="M0,0 L40,0 C80,120 250,195 525,222 L525,300 L0,300 Z" fill="url(#band)"/>
    <path d="M40,0 C80,120 250,195 525,222" fill="none" stroke="url(#edge)" stroke-width="8"/>
  </svg>

  <div class="holder">
    <p class="holder__name">Daniel <span>Morrow-Hale</span></p>
    <p class="holder__role">Managing Partner</p>
  </div>

  <div class="brand">
    <span class="brand__dot"></span>
    <p class="brand__name">BRIM Outreach<br>Partners</p>
  </div>

  <ul class="contacts">
    <li class="contact contact--email">
      <svg class="contact__icon" viewBox="0 0 16 16" aria-hidden="true">
        <circle cx="8" cy="8" r="8" fill="#fff"/>
        <rect x="4" y="5.5" width="8" height="5.5" fill="none" stroke="#6bbbe8" stroke-width="1.2"/>
        <path d="M4 5.5 L8 8.6 L12 5.5" fill="none" stroke="#6bbbe8" stroke-width="1.2"/>
      </svg>
      <span>daniel@brimoutreachpartners.com</span>
    </li>
    <li class="contact contact--phone">
      <svg class="contact__icon" viewBox="0 0 16 16" aria-hidden="true">
        <circle cx="8" cy="8" r="8" fill="#fff"/>
        <path d="M5.2 4.5 L6.8 4.3 L7.4 6.3 L6.5 7 C7 8.2 7.8 9 9 9.5 L9.7 8.6 L11.7 9.2 L11.5 10.8 C8 11 5 8 5.2 4.5 Z" fill="#6bbbe8"/>
      </svg>
      <span>+945-555-0142</span>
    </li>
    <li class="contact contact--place">
      <svg class="contact__icon" viewBox="0 0 16 16" aria-hidden="true">
        <circle cx="8" cy="8" r="8" fill="#fff"/>
        <path d="M8 3.5 C5.9 3.5 4.8 5 4.8 6.6 C4.8 8.8 8 12.5 8 12.5 C8 12.5 11.2 8.8 11.2 6.6 C11.2 5 10.1 3.5 8 3.5 Z" fill="#6bbbe8"/>
        <circle cx="8" cy="6.6" r="1.2" fill="#fff"/>
      </svg>
      <span>Riverton, GA based ( Central Time)</span>
    </li>
  </ul>
</section>

<section class="card card--back" aria-label="Business card back">
  <div class="brand">
    <span class="brand__dot"></span>
    <p class="brand__name">BRIM Outreach<br>Partners</p>
  </div>
</section>

</body>
</html>
```